Flyer-Design für Schamanismus-Pferde-Musik
Vielen Dank, es war eine tolle Zusammenarbeit, mit vielen kreativen Vorschlägen Seitens der Designerin und einer sehr schnellen, guten Umsetzung meiner Änderungswünsche!
Zielgruppe
Schamanismus-Pferde-Musik
schamanische Heilarbeit im grünen Haus ;-)
Einzel- und Gruppencoaching mit PFERD zur Persönlichkeitsentwicklung
Aufgabenstellung
ich persönlich finde quadratische Flyer sehr schön...

```html
<!DOCTYPE html>
<html lang="de">
<head>
<meta charset="utf-8">
<title>Flyer Schamanismus · Pferde · Musik</title>
<link rel="stylesheet" href="https://fonts.googleapis.com/css2?family=Fira+Sans+Condensed:wght@500;600;700&family=Raleway:wght@400;500;600&display=swap">
<style>
:root{
  --red:#b3202c;
  --ink:#2b2b2b;
  --muted:#555;
  --line:#3a3a3a;
  --paper:#ffffff;
  --backdrop:#e4e4e4;
}
*{box-sizing:border-box;margin:0;padding:0}
html,body{width:1200px;height:2880px;overflow:hidden;background:var(--backdrop)}
body{font-family:"Raleway",sans-serif;color:var(--ink);position:relative}
.spread{position:absolute;left:50px;width:1100px;height:550px;display:flex;background:var(--paper);box-shadow:0 2px 10px rgba(0,0,0,.08)}
.spread--outer{top:830px}
.spread--inner{top:1500px}
.page{position:relative;width:550px;height:550px;overflow:hidden}
.page + .page{border-left:1px solid #eee}
.photo{position:absolute}
.rule{position:absolute;background:var(--line)}
.rule--h{height:1.5px}
.rule--v{width:1.5px}
.heading{font-family:"Fira Sans Condensed",sans-serif;font-weight:700;color:var(--red);position:absolute;text-align:center}
.body-text{position:absolute;font-size:8.6px;line-height:1.38;text-align:center;color:var(--ink)}
.red-box{position:absolute;background:var(--red);color:#fff}
.red-box .title{font-family:"Fira Sans Condensed",sans-serif;font-weight:600}
/* outer spread */
.feedback-title{left:253px;width:240px;top:34px;font-size:26px}
.feedback-text{left:253px;width:240px;top:72px}
.feedback-text p + p{margin-top:14px}
.contact-box{left:50px;top:342px;width:190px;height:208px;padding:12px 10px 0 20px}
.contact-box .title{font-size:15.5px;white-space:nowrap;margin-bottom:14px}
.contact-box .note{font-size:8px;text-align:center;line-height:1.35;margin-bottom:12px}
.contact-box .address{font-size:8.4px;font-weight:600;line-height:1.5}
.contact-box .phone{font-size:8.4px;margin-top:10px;display:flex;align-items:center;gap:4px}
.contact-box .info{font-family:"Fira Sans Condensed",sans-serif;font-weight:600;font-size:14px;margin-top:8px;padding-left:10px}
.contact-box .web{font-size:8px;font-weight:600;display:flex;align-items:center;gap:4px;margin-top:2px}
.brand-name{position:absolute;left:100px;top:48px;font-size:19px;font-weight:400;letter-spacing:3px;color:#fff}
.brand-mark{position:absolute;left:60px;top:50px;width:18px;height:18px;border-radius:50%;border:1.5px solid #fff}
.topic-box{left:198px;top:238px;width:178px;height:74px;display:flex;align-items:center;justify-content:center;text-align:center}
.topic-box .title{font-size:14px;line-height:1.25}
/* inner spread */
.motto-box{left:274px;top:37px;width:243px;height:52px;display:flex;align-items:center;justify-content:center;text-align:center}
.motto-box .title{font-size:13.5px;line-height:1.25}
.heal-title{left:274px;width:243px;top:104px;font-size:20px}
.heal-text{left:280px;width:232px;top:140px}
.heal-text p + p{margin-top:10px}
.offers-title{left:50px;width:224px;top:292px;font-size:21px}
.offer-list{position:absolute;left:50px;top:333px;list-style:none}
.offer-list li{display:flex;align-items:center;gap:10px;font-size:10.2px;height:26.5px}
.event-box{left:4px;top:419px;width:252px;height:108px;padding:8px 10px;text-align:center;font-size:6.8px;line-height:1.35}
.event-box .title{font-size:9px;margin:6px 0 4px}
.event-box .last{margin-top:7px}
.horse-title{left:270px;width:221px;top:42px;font-size:21px}
.horse-col{position:absolute;left:270px;width:221px;top:76px;text-align:center}
.horse-col .sub{font-size:8px;line-height:1.35;color:var(--muted)}
.horse-col .warn{font-size:8px;color:var(--red);margin-top:14px}
.horse-col .warn-sub{font-size:8px;margin-top:2px}
.horse-col .lead{font-size:10.4px;line-height:1.32;margin-top:14px}
.offer{position:absolute;left:270px;width:221px}
.offer .name{font-family:"Fira Sans Condensed",sans-serif;font-weight:600;font-size:10px;color:var(--red);border-bottom:1px solid #888;padding-bottom:2px}
.offer .target{display:flex;gap:6px;font-size:7.8px;line-height:1.35;margin-top:4px;padding-left:2px}
.offer .target b{font-weight:500;color:var(--red)}
.offer .dot{flex:0 0 7px;height:7px;background:var(--line);margin-top:2px;border-radius:50%}
</style>
</head>
<body>

<section class="spread spread--outer">
  <div class="page">
    <div class="rule rule--h" style="left:42px;top:20px;width:452px"></div>
    <div class="rule rule--v" style="left:34px;top:30px;height:520px"></div>
    <div class="rule rule--v" style="left:514px;top:30px;height:520px"></div>

    <div class="photo" role="img" aria-label="Frau spielt Geige, Schwarzweiß-Porträt im Seitenprofil" style="left:50px;top:37px;width:190px;height:293px;background:linear-gradient(135deg,#3a2b24,#8a6a56 55%,#1b1512)"></div>
    <h2 class="heading feedback-title">Feedback</h2>
    <div class="body-text feedback-text">
      <p>„Ich dachte, ich kann die Gelegenheit nutzen, um mich nochmal persönlich bei dir zu bedanken! Es war offensichtlich genau das was ich gebraucht hab! Hab danach einiges im Leben geändert, wozu mir sonst immer der Mut, die Kraft und Energie gefehlt hat! Ich habe einen neuen Job ab August, genau das was ich gesucht hab! Ich habe mich von meinem Freund getrennt, was ich schon früher hätte machen sollen! Und ich habe einen ganz besonderen Menschen getroffen, wir lernen uns gerade näher kennen und treffen uns oft! Ich wohne seit dem Wochenende jetzt in einer neuen kleinen Wohnung! Fühle mich richtig gut! Manchmal braucht man einfach wirklich nur eine Auszeit, um Ruhe und Kraft zu tanken! Danke dafür und ganz besonders für die Flussreise!“</p>
      <p>„Mir hat die Möglichkeit mich so unbefangen den Pferden zu nähern die schönsten Erfahrungen gebracht. Das dauert bis ich alles verstanden habe, aber es tat sehr gut und ich schöpfe Kraft daraus.“</p>
    </div>

    <div class="red-box contact-box">
      <div class="title">Die mit der Geige tanzt</div>
      <p class="note">bekannt durch die von ihr<br>mitgegründete Band <b>Nebelharfe</b></p>
      <p class="address">Birte Lhovsmann<br>Lindenhang 7<br>94471 Talhausen (Moorbach)</p>
      <p class="phone"><svg width="8" height="8" viewBox="0 0 10 10"><path d="M2 1l2 2-1 1.5c.8 1.4 1.7 2.3 3 3L7.5 6l2 2-1.2 1.5C4.5 9 1 5.5.5 2.2z" fill="#fff"/></svg>0170/5550148</p>
      <p class="info">Info &amp; Anmeldung</p>
      <p class="web"><svg width="8" height="8" viewBox="0 0 10 10"><circle cx="5" cy="5" r="4.2" fill="none" stroke="#fff" stroke-width="1.2"/></svg>www.wald-ross-klang.de</p>
    </div>
    <div class="photo" role="img" aria-label="Frau streichelt ein weißes Pony auf der Weide" style="left:253px;top:342px;width:261px;height:208px;background:linear-gradient(160deg,#5d6b3c,#c9c6bb 55%,#6c6a58)"></div>
  </div>

  <div class="page">
    <div class="rule rule--h" style="left:56px;top:20px;width:438px"></div>
    <div class="rule rule--h" style="left:56px;top:524px;width:438px"></div>
    <div class="rule rule--v" style="left:30px;top:40px;height:470px"></div>
    <div class="rule rule--v" style="left:520px;top:40px;height:470px"></div>

    <div class="photo" role="img" aria-label="Grünes Holzhaus am Waldrand hinter einer Wiese" style="left:56px;top:37px;width:438px;height:193px;background:linear-gradient(180deg,#38452c 0%,#4f5e36 55%,#a89a63 80%,#8c8250)">
      <span class="brand-mark"></span>
      <span class="brand-name">birte lhovsmann</span>
    </div>
    <div class="photo" role="img" aria-label="Kopf eines weißen Pferdes in Nahaufnahme" style="left:56px;top:238px;width:133px;height:266px;background:linear-gradient(160deg,#efeae2,#a99e90 60%,#5a5046)"></div>
    <div class="red-box topic-box"><div class="title">schamanische Heilarbeit<br>und pferdegestützte<br>Persönlichkeitsentwicklung</div></div>
    <div class="photo" role="img" aria-label="Frau mit Rahmentrommel und schwarzer Hund im Garten" style="left:198px;top:320px;width:178px;height:184px;background:linear-gradient(170deg,#7a4a35,#6d7a4e 55%,#8c8a80)"></div>
    <div class="photo" role="img" aria-label="Hand mit Federschmuck vor einem braunen Pferd" style="left:384px;top:238px;width:110px;height:266px;background:linear-gradient(165deg,#a6572a,#5b76a0 60%,#c6a088)"></div>
  </div>
</section>

<section class="spread spread--inner">
  <div class="page">
    <div class="rule rule--h" style="left:42px;top:20px;width:478px"></div>
    <div class="rule rule--v" style="left:34px;top:30px;height:520px"></div>

    <div class="photo" role="img" aria-label="Frau sitzt meditierend im Wald zwischen Bäumen" style="left:50px;top:36px;width:224px;height:235px;background:linear-gradient(170deg,#6b5a4c,#8d9a66 55%,#4f6a35)"></div>
    <div class="red-box motto-box"><div class="title">Schamanismus ist keine Religion,<br>es ist eine Lebenseinstellung!</div></div>
    <h2 class="heading heal-title">Schamanische Heilarbeit:</h2>
    <div class="body-text heal-text">
      <p>Eins sein mit der Natur und allen Wesen um uns. Jeder Baum, jeder Stein, jedes Tier hat eine Seele. Auch unsere Ahnen spielen eine große Rolle.</p>
      <p>In der schamanischen Ansicht hängen Körper und Seele zusammen, somit haben alle Beschwerden ihren Ursprung in uns. Der Schamane verbindet sich mit der geistigen Welt und lässt seine heilenden Kräfte von dieser leiten.</p>
    </div>
    <div class="photo" role="img" aria-label="Menschen um ein Lagerfeuer in der Dämmerung" style="left:274px;top:271px;width:225px;height:240px;background:linear-gradient(180deg,#3d4a66,#b2431d 55%,#2a1610)"></div>

    <h2 class="heading offers-title">Angebote:</h2>
    <ul class="offer-list">
      <li><svg width="12" height="12" viewBox="0 0 12 12"><rect x="1" y="1" width="10" height="10" rx="5" fill="none" stroke="var(--ink)" stroke-width="1"/><path d="M3.5 6l2 2 5-6" fill="none" stroke="var(--ink)" stroke-width="1.4"/></svg>Chakrenreinigung</li>
      <li><svg width="12" height="12" viewBox="0 0 12 12"><rect x="1" y="1" width="10" height="10" rx="5" fill="none" stroke="var(--ink)" stroke-width="1"/><path d="M3.5 6l2 2 5-6" fill="none" stroke="var(--ink)" stroke-width="1.4"/></svg>Rückholung verlorener Seelenanteile</li>
      <li><svg width="12" height="12" viewBox="0 0 12 12"><rect x="1" y="1" width="10" height="10" rx="5" fill="none" stroke="var(--ink)" stroke-width="1"/><path d="M3.5 6l2 2 5-6" fill="none" stroke="var(--ink)" stroke-width="1.4"/></svg>Heilsteinreinigung</li>
      <li><svg width="12" height="12" viewBox="0 0 12 12"><rect x="1" y="1" width="10" height="10" rx="5" fill="none" stroke="var(--ink)" stroke-width="1"/><path d="M3.5 6l2 2 5-6" fill="none" stroke="var(--ink)" stroke-width="1.4"/></svg>Heilarbeit mit Tieren</li>
      <li><svg width="12" height="12" viewBox="0 0 12 12"><rect x="1" y="1" width="10" height="10" rx="5" fill="none" stroke="var(--ink)" stroke-width="1"/><path d="M3.5 6l2 2 5-6" fill="none" stroke="var(--ink)" stroke-width="1.4"/></svg>Hausreinigung</li>
      <li><svg width="12" height="12" viewBox="0 0 12 12"><rect x="1" y="1" width="10" height="10" rx="5" fill="none" stroke="var(--ink)" stroke-width="1"/><path d="M3.5 6l2 2 5-6" fill="none" stroke="var(--ink)" stroke-width="1.4"/></svg>schamanische Reisen</li>
      <li><svg width="12" height="12" viewBox="0 0 12 12"><rect x="1" y="1" width="10" height="10" rx="5" fill="none" stroke="var(--ink)" stroke-width="1"/><path d="M3.5 6l2 2 5-6" fill="none" stroke="var(--ink)" stroke-width="1.4"/></svg>Arbeit mit Krafttieren</li>
      <li><svg width="12" height="12" viewBox="0 0 12 12"><rect x="1" y="1" width="10" height="10" rx="5" fill="none" stroke="var(--ink)" stroke-width="1"/><path d="M3.5 6l2 2 5-6" fill="none" stroke="var(--ink)" stroke-width="1.4"/></svg>Persönlichkeitsfindung</li>
    </ul>
  </div>

  <div class="page">
    <div class="rule rule--h" style="left:270px;top:20px;width:221px"></div>
    <div class="rule rule--v" style="left:520px;top:40px;height:470px"></div>

    <div class="photo" role="img" aria-label="Geigerin sitzt auf einem schwarzen Pferd im Wald" style="left:4px;top:22px;width:252px;height:397px;background:linear-gradient(175deg,#3f5a2a,#6a7e3c 40%,#1e1f1a 75%,#2d2a22)"></div>
    <div class="red-box event-box">
      <p>Heilsitzungen sind auch aus der Ferne möglich! Dazu machen wir einen Termin aus, an dem sie sich an einem ungestörten Ort Ihrer Wahl für ca eine Stunde Zeit nehmen müssen.</p>
      <p class="title">Veranstaltungen jeden Monat:</p>
      <p>Naturtage, Rauhnachtszeremonie, Feuerzeremonie,<br>Vollmondtrommeln, Frauenkreise</p>
      <p class="last">Regelmäßige offene Gruppen, Zeremonien, Rituale, Trommeln...</p>
    </div>

    <h2 class="heading horse-title">Pferde</h2>
    <div class="horse-col">
      <p class="sub">(Sprenge Deine Grenzen &amp; lebe Deinen<br>Traum / Baue Dein Team / Die Kunst des Führens)</p>
      <p class="warn">KEINE Reiterfahrung oder Pferdekenntnis notwendig</p>
      <p class="warn-sub">Wir machen alle Übungen vom Boden aus!</p>
      <p class="lead">Pferde sind die Spiegel unserer Seele, nur wenn wir authentisch sind wird ein Pferd mit uns freiwillig Kontakt aufnehmen. Diese wunderbaren, kraftvollen Wesen helfen uns innerste Wünsche aufzudecken, Trauer zu verarbeiten, Kraft zu tanken und die wahrhafte Kommunikation wieder zu erlernen, die nichts mit viel reden zu tun hat!</p>
    </div>
    <div class="offer" style="top:300px">
      <p class="name">Sprenge Deine Grenzen &amp; Lebe Deinen Traum!</p>
      <p class="target"><span class="dot"></span><span><b>Zielgruppe:</b> Privatpersonen, die etwas in ihrem Leben verändern wollen, aber noch nach dem Weg dahin suchen</span></p>
    </div>
    <div class="offer" style="top:370px">
      <p class="name">Baue Deinen Traum</p>
      <p class="target"><span class="dot"></span><span><b>Zielgruppe:</b> jegliche Zusammensetzungen von Gruppen, ob Jugendgruppen, Bands, Kommunen, Familien...</span></p>
    </div>
    <div class="offer" style="top:450px">
      <p class="name">Die Kunst des Führens</p>
      <p class="target"><span class="dot"></span><span><b>Zielgruppe:</b> alle „Führungskräfte“, Lehrer, Mütter, etc. die eine Gruppe zu leiten haben</span></p>
    </div>
  </div>
</section>

</body>
</html>
```